verdant terraces simple classy business card design

my name is owen harlow and I run a gardening business aimed at high class verdant terraces. the business name is verdant terraces and our logo was designed on pixel forum .My clientel are anything from residential homes to businesses. I take pride in my work and know that I offer a service like no other in my area.
The business card will be used to represent my business and I want it to be not only rememberable, but simplistic and modern. Eye catching too. Of course I would like it relatable to gardening and appealing to the correct clientel - those being garden enthusiasts, prestigious homes and businesses that are after top of the line gardening services like no other on the market.
I am not a typical lawn mowing business so I don't want a typical card design that represents that. The gardens I work with are generally million dollar properties with owners who are very garden proud looking for upkeep and guidance from me along with sometimes whole new garden designs. I want the business cards to show to my clients that I take pride, as they do, in their garden. And I want them to know from my card that I am a professional, qualified horticulturist offering them a top of the line service for life. I want them to refer my business on. I want them to look at my business card and see class and professionalism in a modern unique bold way.
The card should be simple with the possibility of the logo on the front being embossed/debossed and my details on the back the card should have a organic garden feel it's very important to me that it is absolutely perfect
I am also very open to ideas and suggestions so look forward to seeing the designs. the business logo has been supplied with this project and I want the card to be double sided

Contact info is
Owen Harlow - Managing Director / Horticulturist
Phone : 0481 526 704
Email: owenharlow@verdantterraces.com.au

Target Market(s)

high class gardens residential and commercial

Industry/Entity Type

Gardener

Contact Information for Business Card

Contact info is
Phone : 0481 526 704

PLEASE MAKE CARD DOUBLE SIDED

Requirements
Must have
• organic simple classy modern feel
• must flow with the current logo that has been supplied with this project
• Double sided
• Must explain in a simple way that I deal with high end gardens and I'm a qualified horticulturist
Nice to have
• embossed debossed logo
Should not have
• shouldn't be to busy or cheap looking

```html
<!DOCTYPE html>
<html lang="en">
<head>
<meta charset="utf-8">
<title>Verdant Terraces – Business Card</title>
<link rel="stylesheet" href="https://fonts.googleapis.com/css2?family=Montserrat:wght@400;600;700&display=swap">
<style>
  :root {
    --page: #2b2b2b;
    --card-front: #e6e7e9;
    --emboss: #d2d4d7;
    --card-back: #ffffff;
    --leaf: #5d9f5f;
    --leaf-deep: #3f8f45;
    --on-leaf: #ffffff;
  }
  * { box-sizing: border-box; margin: 0; padding: 0; }
  html, body { width: 1200px; height: 900px; overflow: hidden; }
  body {
    background: var(--page);
    font-family: "Montserrat", Arial, sans-serif;
    position: relative;
  }
  .card {
    position: absolute;
    width: 560px;
    height: 320px;
    border-radius: 22px;
    overflow: hidden;
  }
  .card--front {
    left: 80px;
    top: 110px;
    background: var(--card-front);
    display: flex;
    align-items: center;
    justify-content: center;
    gap: 16px;
  }
  .front-mark {
    width: 46px; height: 46px;
    border-radius: 50%;
    background: var(--emboss);
  }
  .front-name {
    color: var(--emboss);
    font-weight: 600;
    font-size: 30px;
    letter-spacing: 4px;
    text-transform: uppercase;
    line-height: 1.15;
  }
  .card--back {
    left: 560px;
    top: 480px;
    background: var(--card-back);
  }
  .brand {
    position: absolute;
    right: 36px;
    top: 46px;
    display: flex;
    align-items: center;
    gap: 12px;
  }
  .brand-mark {
    width: 40px; height: 40px;
    border-radius: 50%;
    background: var(--leaf);
  }
  .brand-name {
    color: var(--leaf-deep);
    font-weight: 600;
    font-size: 22px;
    letter-spacing: 3px;
    text-transform: uppercase;
    line-height: 1.2;
  }
  .divider {
    position: absolute;
    left: 0; right: 0;
    top: 196px;
    height: 4px;
    background: var(--leaf);
  }
  .contact-band {
    position: absolute;
    left: 0; right: 0; bottom: 0;
    height: 112px;
    background: var(--leaf);
    color: var(--on-leaf);
    padding: 14px 0 0 40px;
  }
  .person-name { font-weight: 700; font-size: 24px; line-height: 1.1; }
  .person-role { font-size: 13px; margin: 3px 0 8px; }
  .contact-line {
    display: flex; align-items: center; gap: 8px;
    font-size: 13px; line-height: 1.5;
  }
  .contact-line svg { width: 11px; height: 11px; fill: var(--on-leaf); }
</style>
</head>
<body>
  <section class="card card--front" aria-label="Card front">
    <span class="front-mark"></span>
    <span class="front-name">Verdant<br>Terraces</span>
  </section>

  <section class="card card--back" aria-label="Card back">
    <div class="brand">
      <span class="brand-mark"></span>
      <span class="brand-name">Verdant<br>Terraces</span>
    </div>
    <div class="divider"></div>
    <div class="contact-band">
      <p class="person-name">Owen Harlow</p>
      <p class="person-role">Managing Director / Horticulturist</p>
      <p class="contact-line">
        <svg viewBox="0 0 24 24" aria-hidden="true"><path d="M6.6 10.8a15.1 15.1 0 0 0 6.6 6.6l2.2-2.2c.3-.3.7-.4 1-.2 1.1.4 2.3.6 3.6.6.6 0 1 .4 1 1V20c0 .6-.4 1-1 1A17 17 0 0 1 3 4c0-.6.4-1 1-1h3.5c.6 0 1 .4 1 1 0 1.3.2 2.5.6 3.6.1.3 0 .7-.2 1z"/></svg>
        0481 526 704
      </p>
      <p class="contact-line">
        <svg viewBox="0 0 24 24" aria-hidden="true"><path d="M2 5h20v14H2zm2 2v.5l8 5 8-5V7zm0 2.8V17h16V9.8l-8 5z"/></svg>
        owenharlow@verdantterraces.com.au
      </p>
    </div>
  </section>
</body>
</html>
```